Training Company Needs a Web Design

We are a Training company that needs a website design completed for us. "The Harbor Loft" The website will be a 'community space' specialising in 'Change and Transformation'. It will be a 'space' where individuals can come to find out 'latest news', upcoming events and courses, chat with others and find 'tools and templates'. They will need to login as a 'Member'.

The final design needs to be professional but have a 'fun and interactive' feel and appeal to our target audience who are predominantly corporate individuals.

Target Market(s)

Corporate Individuals - they may have a Change or Project background

Industry/Entity Type

Business Consultant

Number of Pages Required

3 page

Font styles to use
Sans Serif

Requirements
Must have
• Design for 'Home Page'
• A professional and corporate 'feel' but be fun and interactive.
Nice to have
• A 'sense' of how some of the other pages may be designed or laid out.

```html
<!DOCTYPE html>
<html lang="en">
<head>
<meta charset="utf-8">
<title>The Harbor Loft — Home</title>
<link href="https://fonts.googleapis.com/css2?family=Saira:wght@400;500;600;800&family=Lato:wght@400;700&display=swap" rel="stylesheet">
<style>
:root{
  --blue:#0a8fd0;
  --blue-deep:#0b5f9c;
  --navy:#0c3f6e;
  --ink:#2b2b2b;
  --text:#4a4a4a;
  --muted:#777;
  --rule:#d6d6d6;
  --panel:#eeeeee;
  --card:#ececec;
  --dark:#2e2e2e;
  --darker:#1f1f1f;
  --btn:#151515;
  --white:#fff;
}
*{box-sizing:border-box;margin:0;padding:0}
html,body{width:1200px;height:2616px;overflow:hidden}
body{position:relative;background:var(--white);font-family:'Lato',sans-serif;color:var(--text)}
.abs{position:absolute}
.heading{font-family:'Saira',sans-serif;font-weight:400;text-transform:uppercase;color:var(--blue);letter-spacing:.5px}
.heading b{font-weight:400;color:var(--navy)}
.btn{position:absolute;background:var(--btn);color:var(--white);font:700 12px 'Lato',sans-serif;text-transform:uppercase;display:flex;align-items:center;justify-content:center;border-radius:2px;letter-spacing:.5px}

/* header */
.site-header{position:absolute;left:0;top:0;width:1200px;height:117px;background:linear-gradient(#fafafa,#dedede)}
.brand{position:absolute;left:166px;top:30px;display:flex;align-items:center;gap:10px;font:600 22px/1.05 'Saira',sans-serif;color:var(--blue-deep);text-transform:uppercase}
.brand-mark{width:18px;height:18px;background:var(--blue)}
.pill{position:absolute;top:21px;height:35px;border:1px solid #9a9a9a;border-radius:18px;background:linear-gradient(#fff,#e4e4e4);display:flex;align-items:center;justify-content:center;gap:8px;font:700 12px 'Lato',sans-serif;color:#333;text-transform:uppercase}
.contact-bit{position:absolute;top:70px;display:flex;align-items:center;gap:8px;font:700 12px/1.2 'Lato',sans-serif;color:#222}
.contact-bit small{display:block;font-weight:400;font-size:11px}
.ico-dot{width:24px;height:24px;border-radius:50%;background:var(--navy);display:flex;align-items:center;justify-content:center}

/* nav */
.main-nav{position:absolute;left:0;top:117px;width:1200px;height:42px;background:linear-gradient(var(--blue-deep),var(--navy))}
.main-nav a{position:absolute;top:0;height:42px;display:flex;align-items:center;justify-content:center;color:var(--white);font:400 15px 'Lato',sans-serif;text-decoration:none;text-transform:uppercase;border-left:1px solid rgba(255,255,255,.25)}
.main-nav a.current{background:#151515;border-left:none}

/* hero */
.hero{position:absolute;left:0;top:159px;width:1200px;height:443px;background:linear-gradient(120deg,#5a5a5a,#8a8a8a 45%,#3e3e3e)}
.hero h1{position:absolute;left:0;right:0;top:152px;text-align:center;font:400 43px/1.45 'Saira',sans-serif;color:var(--white);text-transform:uppercase}
.dot{position:absolute;top:569px;width:14px;height:14px;border-radius:50%;background:var(--blue)}
.dot.off{background:transparent;border:2px solid #ddd}

/* welcome */
.thumb{position:absolute;top:689px;width:269px;height:145px;border:5px solid #fff;box-shadow:0 0 0 1px #ccc,0 2px 4px rgba(0,0,0,.15)}
.sub-title{position:absolute;width:269px;text-align:center;top:850px;font:400 19px 'Saira',sans-serif;color:var(--blue);text-transform:uppercase}
.sub-title b{font-weight:400;color:var(--navy)}
.blurb{position:absolute;top:884px;width:280px;font-size:12px;line-height:19px;text-align:center;color:#444}
.inquiry{position:absolute;left:769px;top:640px;width:271px;height:354px;background:#fff;border:1px solid #e2e2e2;box-shadow:0 4px 8px rgba(0,0,0,.15)}
.field{position:absolute;left:19px;width:232px;border:1px dashed #bdbdbd;font-size:11px;color:#444;padding-left:36px;display:flex;align-items:center}
.field svg{position:absolute;left:10px}

/* tools */
.tools{position:absolute;left:0;top:1046px;width:1200px;height:306px;background:var(--panel);border-top:3px solid #fff}
.divider-dot{position:absolute;width:12px;height:12px;border:2px solid var(--blue);border-radius:50%;background:#fff}
.select{position:absolute;left:485px;top:1224px;width:232px;height:37px;border:1px dashed #aaa;background:#fff;font-size:11px;color:#444;padding-left:14px;display:flex;align-items:center}

/* feature panels */
.feature{position:absolute;top:1352px;width:600px;height:336px;color:#fff;text-align:center}
.feature h3{position:absolute;left:0;right:0;top:124px;font:800 24px 'Saira',sans-serif;letter-spacing:1px;text-transform:uppercase}
.feature p{position:absolute;left:90px;right:90px;top:172px;font-size:14px;line-height:26px}

/* lists */
.why-list{position:absolute;left:166px;top:1814px;list-style:none}
.why-list li{height:35px;display:flex;align-items:center;gap:16px;font-size:14px;color:#222}
.event{position:absolute;left:616px;width:424px;height:134px;background:var(--card);border-radius:3px}
.event .avatar{position:absolute;left:12px;top:19px;width:96px;height:96px;border-radius:50%;border:4px solid var(--blue-deep);background:radial-gradient(circle at 40% 40%,#e8c9a8,#b8866a 55%,#6d7e92)}
.event .meta{position:absolute;left:132px;top:20px;font:italic 10px 'Lato',sans-serif;color:var(--blue)}
.event h4{position:absolute;left:132px;top:42px;font:700 11px 'Lato',sans-serif;color:#222;text-transform:uppercase}
.event p{position:absolute;left:132px;top:62px;width:272px;font-size:10px;line-height:16px;color:#555}

/* footer */
.footer-head{position:absolute;top:2340px;font:400 13px 'Lato',sans-serif;color:#fff;text-transform:uppercase;border-bottom:1px solid #555;padding-bottom:7px}
.quick-links{position:absolute;left:167px;top:2372px;list-style:none}
.quick-links li{height:27px;font-size:11px;color:#eee}
.quick-links li::before{content:"• ";color:#eee}
.quick-links li.current{color:#5bb8ea}
.social{position:absolute;left:916px;display:flex;align-items:center;gap:14px;color:#fff;font:400 12px/1.05 'Lato',sans-serif;text-transform:uppercase}
.social i{width:28px;height:28px;border-radius:50%;background:var(--blue-deep);display:block}
.social small{display:block;font-size:8px}
.copyright{position:absolute;left:0;top:2578px;width:1200px;height:38px;background:var(--navy);color:#fff;font-size:11px;display:flex;align-items:center;justify-content:center;text-transform:uppercase;letter-spacing:.3px}
</style>
</head>
<body>

<header class="site-header">
  <div class="brand"><span class="brand-mark"></span><span>The Harbor Loft</span></div>
  <div class="pill" style="left:790px;width:108px">
    <svg width="12" height="14" viewBox="0 0 12 14"><rect x="1" y="6" width="10" height="8" rx="1" fill="#222"/><path d="M3 6V4a3 3 0 0 1 6 0v2" stroke="#222" stroke-width="1.6" fill="none"/></svg>Login</div>
  <div class="pill" style="left:917px;width:123px">
    <svg width="14" height="14" viewBox="0 0 14 14"><circle cx="7" cy="4" r="3.2" fill="#222"/><path d="M1 14c0-4 3-6 6-6s6 2 6 6z" fill="#222"/></svg>Register</div>
  <div class="contact-bit" style="left:733px">
    <span class="ico-dot"><svg width="12" height="12" viewBox="0 0 12 12"><path d="M2 1l2.5 0 1 3-1.5 1a7 7 0 0 0 3 3l1-1.5 3 1V11.5C5 11.5 .5 7 2 1z" fill="#fff"/></svg></span>
    <span><small>Call Us</small>(555) 214 - 3096</span></div>
  <div class="contact-bit" style="left:881px;top:75px">
    <span class="ico-dot"><svg width="12" height="9" viewBox="0 0 12 9"><rect width="12" height="9" fill="#fff"/><path d="M0 0l6 5 6-5" stroke="#0c3f6e" fill="none"/></svg></span>
    <span>hello@harborloft.com</span></div>
</header>

<nav class="main-nav">
  <a class="current" style="left:162px;width:100px">Home</a>
  <a style="left:262px;width:130px">About Us</a>
  <a style="left:392px;width:126px">Services</a>
  <a style="left:518px;width:126px">Training</a>
  <a style="left:644px;width:132px">Careers</a>
  <a style="left:776px;width:112px">E-Store</a>
  <a style="left:888px;width:152px;border-right:1px solid rgba(255,255,255,.25)">Contact Us</a>
</nav>

<section class="hero" role="img" aria-label="Photograph of a person in a patterned top using a tablet at an office desk">
  <h1>We Specialize in Change &amp;<br>Transformation</h1>
</section>
<span class="dot off" style="left:556px"></span>
<span class="dot" style="left:581px"></span>
<span class="dot" style="left:603px"></span>
<span class="dot" style="left:628px"></span>

<section class="welcome">
  <h2 class="heading abs" style="left:160px;top:632px;font-size:30px">Welcome to <b>The Harbor Loft</b></h2>
  <div class="thumb" style="left:160px;background:linear-gradient(#e9ecef,#9aa3ab 60%,#3b3f45)" role="img" aria-label="Photograph of a business team standing together"></div>
  <div class="thumb" style="left:460px;background:linear-gradient(120deg,#222,#5a5a5a 60%,#1a1a1a)" role="img" aria-label="Photograph of a businessman on a phone call"></div>
  <div class="sub-title" style="left:160px">Who <b>We Are</b></div>
  <div class="sub-title" style="left:460px">Our <b>Mission</b></div>
  <p class="blurb" style="left:155px">Lorem ipsum dolor sit amet, consectet uer adipiscing elit, sed diam nonummy nibh euis mod tincidun nt ut laoreetml dolore magna aliquam erat volutpat.</p>
  <p class="blurb" style="left:455px">Lorem ipsum dolor sit amet, consectet uer adipiscing elit, sed diam nonummy nibh euis mod tincidun nt ut laoreetml dolore magna aliquam erat volutpat.</p>
  <div class="btn" style="left:249px;top:956px;width:100px;height:31px">Read More</div>
  <div class="btn" style="left:554px;top:956px;width:100px;height:31px">Read More</div>

  <form class="inquiry">
    <h3 class="heading abs" style="left:18px;top:10px;font-size:23px">Quick <b>Inquiry</b></h3>
    <div class="field" style="top:52px;height:37px"><svg width="10" height="11" viewBox="0 0 10 11"><circle cx="5" cy="3" r="2.5" fill="#555"/><path d="M0 11c0-3 2-5 5-5s5 2 5 5z" fill="#555"/></svg>Name</div>
    <div class="field" style="top:96px;height:38px"><svg width="11" height="8" viewBox="0 0 11 8"><rect width="11" height="8" fill="#555"/><path d="M0 0l5.5 4 5.5-4" stroke="#fff" fill="none"/></svg>Email</div>
    <div class="field" style="top:141px;height:37px"><svg width="10" height="10" viewBox="0 0 12 12"><path d="M2 1l2.5 0 1 3-1.5 1a7 7 0 0 0 3 3l1-1.5 3 1V11.5C5 11.5 .5 7 2 1z" fill="#555"/></svg>Phone</div>
    <div class="field" style="top:187px;height:106px;align-items:flex-start;padding-top:12px"><svg width="10" height="10" viewBox="0 0 10 10" style="top:12px"><rect x=".5" y="1.5" width="8" height="8" fill="none" stroke="#555"/><path d="M4 6l5-5" stroke="#555" stroke-width="1.4"/></svg>Message</div>
    <div class="btn" style="left:19px;top:305px;width:98px;height:32px">Submit</div>
  </form>
</section>

<section class="tools">
  <h2 class="heading abs" style="left:0;width:1200px;text-align:center;top:28px;font-size:30px">Find Tools <b>and Templates</b></h2>
  <span class="divider-dot" style="left:594px;top:78px"></span>
  <p class="abs" style="left:180px;width:840px;top:104px;text-align:center;font-size:15px;line-height:29px;color:#444">Duis autem vel eum iriure &nbsp;ehendreritin vulputate velit esse molestie consequat, vel illum dolore eu feugiat nulla facilisis at vero eros et a &nbsp;molestie consequat,n et iusto &nbsp;velit esse molestie consequat, vel illum dolore</p>
</section>
<div class="select">Tools And Templates
  <svg class="abs" style="right:0;top:0" width="40" height="35" viewBox="0 0 40 35"><line x1="0" y1="0" x2="0" y2="35" stroke="#aaa" stroke-dasharray="3 2"/><path d="M14 14h12l-6 7z" fill="#888"/></svg></div>
<div class="btn" style="left:548px;top:1285px;width:106px;height:33px">Get Started</div>

<section class="feature" style="left:0;background:linear-gradient(rgba(20,70,130,.82),rgba(14,60,115,.9)),linear-gradient(90deg,#c9d5e2,#6f8aa8)" role="img" aria-label="Photograph of a trainer presenting to colleagues in a meeting room">
  <svg class="abs" style="left:270px;top:42px" width="62" height="62" viewBox="0 0 62 62" fill="none" stroke="#fff" stroke-width="7">
    <path d="M2 14h14c14 0 16 34 30 34h8"/><path d="M2 48h14c14 0 16-34 30-34h8"/>
    <path d="M50 4l10 10-10 10M50 38l10 10-10 10" stroke-width="5"/></svg>
  <h3>Change</h3>
  <p>Duis autem vel eum iriure &nbsp;ehendreritin vulputate velit esse molestie consequat, vel illum dolore eu feugiat nulla facilisis at vero eros et a &nbsp;molestie consequat,n et iusto</p>
  <div class="btn" style="left:332px;top:268px;width:100px;height:30px">Read More</div>
</section>
<section class="feature" style="left:600px;background:linear-gradient(135deg,#0a9bd8,#0b7fc0 60%,#0a6aab)" role="img" aria-label="Illustration of blue geometric cubes">
  <svg class="abs" style="left:266px;top:40px" width="70" height="70" viewBox="0 0 70 70" fill="none" stroke="#fff">
    <circle cx="42" cy="26" r="14" stroke-width="8" stroke-dasharray="5 4"/><circle cx="42" cy="26" r="8" stroke-width="3"/>
    <circle cx="16" cy="54" r="9" stroke-width="6" stroke-dasharray="4 3"/><circle cx="16" cy="54" r="4" stroke-width="2"/></svg>
  <h3>Transformation</h3>
  <p>Duis autem vel eum iriure &nbsp;ehendreritin vulputate velit esse molestie consequat, vel illum dolore eu feugiat nulla facilisis at vero eros et a &nbsp;molestie consequat,n et iusto</p>
  <div class="btn" style="left:176px;top:268px;width:100px;height:30px">Read More</div>
</section>

<section class="why">
  <h2 class="heading abs" style="left:160px;width:424px;text-align:center;top:1720px;font-size:30px">Why <b>Choose Us?</b></h2>
  <div class="abs" style="left:160px;top:1777px;width:424px;border-top:1px solid var(--rule)"></div>
  <span class="divider-dot" style="left:366px;top:1771px"></span>
  <ul class="why-list">
    <li><svg width="22" height="16" viewBox="0 0 22 16"><path d="M2 8l6 6L20 2" stroke="#0b7fc0" stroke-width="3" fill="none"/></svg>Lorem ipsum dolor sit amet, consectet</li>
    <li><svg width="22" height="16" viewBox="0 0 22 16"><path d="M2 8l6 6L20 2" stroke="#0b7fc0" stroke-width="3" fill="none"/></svg>Lorem ipsum dolor sit amet, consectet &nbsp;dolor sit ame</li>
    <li><svg width="22" height="16" viewBox="0 0 22 16"><path d="M2 8l6 6L20 2" stroke="#0b7fc0" stroke-width="3" fill="none"/></svg>Lorem ipsum dolor sit amet, consectet &nbsp;nonummy nibh</li>
    <li><svg width="22" height="16" viewBox="0 0 22 16"><path d="M2 8l6 6L20 2" stroke="#0b7fc0" stroke-width="3" fill="none"/></svg>Lorem ipsum dolor sit amet, ectet</li>
    <li><svg width="22" height="16" viewBox="0 0 22 16"><path d="M2 8l6 6L20 2" stroke="#0b7fc0" stroke-width="3" fill="none"/></svg>Lorem ipsum dolor sit amet, consectet ipsum dolor</li>
    <li><svg width="22" height="16" viewBox="0 0 22 16"><path d="M2 8l6 6L20 2" stroke="#0b7fc0" stroke-width="3" fill="none"/></svg>Lorem ipsum dolor sit amet, consectet &nbsp;nonummy nibh</li>
    <li><svg width="22" height="16" viewBox="0 0 22 16"><path d="M2 8l6 6L20 2" stroke="#0b7fc0" stroke-width="3" fill="none"/></svg>Lorem ipsum dit amet, consectet ipsum dolor</li>
    <li><svg width="22" height="16" viewBox="0 0 22 16"><path d="M2 8l6 6L20 2" stroke="#0b7fc0" stroke-width="3" fill="none"/></svg>Lorem ipsum dolor sit amet, consectet</li>
    <li><svg width="22" height="16" viewBox="0 0 22 16"><path d="M2 8l6 6L20 2" stroke="#0b7fc0" stroke-width="3" fill="none"/></svg>Lorem ipsum dolor sit amet, consectet &nbsp;nonummy nibh</li>
  </ul>
</section>

<section class="events">
  <h2 class="heading abs" style="left:616px;width:424px;text-align:center;top:1720px;font-size:30px">Upcoming <b>Events</b></h2>
  <div class="abs" style="left:616px;top:1777px;width:424px;border-top:1px solid var(--rule)"></div>
  <span class="divider-dot" style="left:822px;top:1771px"></span>
  <article class="event" style="top:1824px">
    <div class="avatar" role="img" aria-label="Photograph of two smiling colleagues"></div>
    <div class="meta">23 Feb 2016 &nbsp;/ &nbsp;0 Comments</div>
    <h4>Lorem ipsum dolor &nbsp;consecte</h4>
    <p>Duis autem vel eum iriure dolor in hendreri inmo vulputate velit esse molestie consequat vel illum dolore eu feugiat nulla facilisis... [+]</p>
  </article>
  <article class="event" style="top:1997px">
    <div class="avatar" role="img" aria-label="Photograph of a student at a laptop"></div>
    <div class="meta">23 Feb 2016 &nbsp;/ &nbsp;0 Comments</div>
    <h4>Lorem ipsum dolor &nbsp;consecte</h4>
    <p>Duis autem vel eum iriure dolor in hendreri inmo vulputate velit esse molestie consequat vel illum dolore eu feugiat nulla facilisis... [+]</p>
  </article>
  <span class="abs" style="left:994px;top:2151px;width:9px;height:9px;border-radius:50%;background:var(--blue)"></span>
  <span class="abs" style="left:1008px;top:2152px;width:7px;height:7px;border-radius:50%;background:#ccc"></span>
  <span class="abs" style="left:1020px;top:2152px;width:7px;height:7px;border-radius:50%;background:#ccc"></span>
</section>

<footer>
  <svg class="abs" style="left:0;top:2140px" width="1200" height="440" viewBox="0 0 1200 440">
    <defs><linearGradient id="footerFill" x1="0" y1="0" x2="0" y2="1"><stop offset="0" stop-color="#4a4a4a"/><stop offset=".35" stop-color="#2d2d2d"/><stop offset="1" stop-color="#1d1d1d"/></linearGradient></defs>
    <path d="M0 95C180 50 380 120 560 125S900 110 1200 10V440H0Z" fill="url(#footerFill)"/>
    <path d="M540 120C760 130 980 110 1200 20V0C1000 80 780 118 540 120Z" fill="#0b5f9c"/>
    <path d="M540 120C760 132 980 112 1200 32" stroke="#0a8fd0" stroke-width="3" fill="none"/>
  </svg>
  <div class="abs" style="left:200px;top:2244px;display:flex;align-items:center;gap:10px;font:400 22px 'Saira',sans-serif;color:#8a8a8a;text-transform:uppercase">
    <span style="width:16px;height:16px;background:#8a8a8a;display:block"></span>The Harbor Loft</div>

  <h4 class="footer-head" style="left:167px;width:134px">Quick Links</h4>
  <ul class="quick-links">
    <li class="current">Home</li><li>Services</li><li>Training</li><li>Careers</li><li>E-store</li><li>Contact us</li>
  </ul>

  <h4 class="footer-head" style="left:344px;width:172px">Contact Details</h4>
  <div class="abs" style="left:344px;top:2373px;font-size:11px;line-height:15px;color:#eee"><b>THE HARBOR LOFT</b><br>123, Lorem ipsum dolor si amet,<br>consectetue &nbsp;nibh euismod</div>
  <div class="abs" style="left:344px;top:2440px;display:flex;align-items:center;gap:9px;font-size:15px;color:#fff">
    <svg width="12" height="12" viewBox="0 0 12 12"><path d="M2 1l2.5 0 1 3-1.5 1a7 7 0 0 0 3 3l1-1.5 3 1V11.5C5 11.5 .5 7 2 1z" fill="#fff"/></svg>(555) 214 - 3096</div>
  <div class="abs" style="left:344px;top:2485px;display:flex;align-items:center;gap:9px;font-size:11px;color:#eee">
    <svg width="11" height="8" viewBox="0 0 11 8"><rect width="11" height="8" fill="#fff"/><path d="M0 0l5.5 4 5.5-4" stroke="#333" fill="none"/></svg>hello@harborloft.com</div>

  <h4 class="footer-head" style="left:593px;width:246px">Quick Contact</h4>
  <div class="abs" style="left:593px;top:2381px;width:246px;height:99px;background:linear-gradient(135deg,#ece8df,#dfe6d8);border:3px solid #fff" role="img" aria-label="Street map showing the office location"></div>

  <h4 class="footer-head" style="left:916px;width:124px">Follow Us</h4>
  <div class="social" style="top:2384px"><i></i><span>Circlenet<small>Become a fan</small></span></div>
  <div class="social" style="top:2438px"><i></i><span>Worklink<small>Join us on</small></span></div>
  <div class="social" style="top:2492px"><i></i><span>Chirper<small>Join us on</small></span></div>

  <div class="copyright">© 2016 The Harbor Loft. All rights reserved.</div>
</footer>

</body>
</html>
```